Multifamily Investment Strategies

I need a pamphlet or booklet for multifamily commercial real estate investment.

The specific investment vehicle is affordable multifamily apartments. I have uploaded a 5 page pdf detailing my investment strategy.

The target audience for this pamphlet are investors, commercial brokers, and commercial bankers.

I am looking for modern, clean design that is striking and professional but also eye catching.
Updates

I made a few changes to the brief and also corrected two errors.

Target Market(s)

Commercial Real Estate Investors, Brokers, and Bankers

Industry/Entity Type

Real Estate

Font styles to use
Serif

Colors

Designer to choose colors to be used in the design.

Requirements
Must have
• Graphics of or related to apartment buildings.
• My headshot seen on the last page of the pdf
Nice to have
• Imagery related to investment and profits.
Should not have
• The image of an apartment building on the first page of the pdf is just an example. Please don’t use this image.

```html
<!DOCTYPE html>
<html lang="en">
<head>
<meta charset="utf-8">
<title>Redmont Residential – Investment Strategy Booklet</title>
<link href="https://fonts.googleapis.com/css2?family=Lato:wght@300;400&family=Montserrat:wght@400;500;600;700&display=swap" rel="stylesheet">
<style>
  :root{
    --backdrop:#808080;
    --paper:#ffffff;
    --navy:#2e4374;
    --blue:#1d4f91;
    --orange:#e8860c;
    --ink:#333a44;
    --muted:#5b6270;
    --band:#e6e6e6;
    --frame:#9a9a9a;
    --photo-a:#6f84b6;
    --photo-b:#c9d3e8;
  }
  *{margin:0;padding:0;box-sizing:border-box}
  html,body{width:1200px;height:1200px;overflow:hidden;background:var(--backdrop)}
  body{position:relative;font-family:"Montserrat",Arial,sans-serif;color:var(--ink)}
  .page{position:absolute;background:var(--paper);overflow:hidden}
  .frame{position:absolute;border:1px solid var(--frame);pointer-events:none}
  .footer-bar{position:absolute;bottom:0;height:12px;background:var(--orange)}
  .abs{position:absolute}
  .photo{position:absolute;left:0;width:100%}
  .photo-building{background:linear-gradient(180deg,#3d63a8 0%,#6e8fc4 40%,#8a4a34 41%,#7b4532 72%,#3b3b3d 73%,#222 100%)}
  .photo-houses{background:linear-gradient(160deg,var(--photo-b) 0%,var(--photo-a) 55%,#4e6597 100%)}
  .section-head{position:absolute;background:var(--navy);color:#fff;font-weight:500;letter-spacing:.03em;display:flex;align-items:center;padding-left:7px}
  .step-title{position:absolute;color:var(--blue);font-weight:700;font-size:13px;letter-spacing:.04em}
  .step-title.orange{color:var(--orange)}
  .tick{display:inline-block;width:9px;height:9px;vertical-align:-1px;margin-right:5px;flex:none;margin-top:1px}
  .row{position:absolute;display:flex;align-items:flex-start;line-height:1.35}
  .tiny{font-size:5.4px;line-height:1.4;color:var(--muted)}
  .orange-t{color:var(--orange);font-weight:600}
  .blue-t{color:var(--blue);font-weight:600}
  .white-t{color:#dfe5f0}
  b{font-weight:600}
</style>
</head>
<body>

<svg width="0" height="0" style="position:absolute" aria-hidden="true">
  <symbol id="tick-orange" viewBox="0 0 10 10"><circle cx="5" cy="5" r="4" fill="none" stroke="#e8860c" stroke-width="1"/><path d="M3 5.2l1.6 1.5L8.6 2" fill="none" stroke="#e8860c" stroke-width="1.2"/></symbol>
  <symbol id="tick-navy" viewBox="0 0 10 10"><circle cx="5" cy="5" r="4" fill="none" stroke="#2e4374" stroke-width="1"/><path d="M3 5.2l1.6 1.5L8.6 2" fill="none" stroke="#2e4374" stroke-width="1.2"/></symbol>
</svg>

<!-- Cover -->
<section class="page cover" style="left:52px;top:98px;width:343px;height:480px">
  <div class="frame" style="left:8px;top:8px;width:327px;height:464px"></div>
  <p class="abs" style="left:0;top:22px;width:100%;text-align:center;font-size:8.4px;font-weight:600;color:var(--blue);letter-spacing:.02em">REDMONT RESIDENTIAL INVESTMENT STRATEGY</p>
  <p class="abs" style="left:0;top:62px;width:100%;text-align:center;font-family:'Lato',sans-serif;font-weight:300;font-size:17px;color:#444">Turning Underperforming</p>
  <div class="abs" style="left:34px;top:83px;width:276px;height:24px;background:var(--navy);color:#fff;font-family:'Lato',sans-serif;font-weight:300;font-size:18.5px;text-align:center;line-height:24px;letter-spacing:.02em">MULTIFAMILY PROPERTIES</div>
  <p class="abs" style="left:0;top:116px;width:100%;text-align:center;font-size:16px;line-height:1.25;color:var(--orange);font-weight:700;letter-spacing:.03em"><span style="font-family:'Lato',sans-serif;font-weight:300;color:#333">INTO</span> HIGHLY PROFITABLE,<br>CASH-FLOWING ASSETS.</p>
  <div class="photo photo-building" style="top:171px;height:274px" role="img" aria-label="Photo of a two-storey red brick apartment building with white trim and a parking lot under a blue sky"></div>
  <div class="footer-bar" style="left:28px;width:287px"></div>
</section>

<!-- Steps: Buy right -->
<section class="page" style="left:435px;top:96px;width:342px;height:484px">
  <div class="frame" style="left:8px;top:8px;width:326px;height:468px"></div>
  <div class="section-head" style="left:11px;top:30px;width:216px;height:29px;font-size:16px">3 STEPS FOR SUCCESS</div>
  <div class="step-title" style="left:12px;top:66px">1&nbsp; BUY RIGHT</div>
  <div class="row" style="left:14px;top:88px;font-size:7.6px"><svg class="tick"><use href="#tick-navy"/></svg><span><b>Value Add</b> - <span style="font-size:6px">Key questions when considering a property:</span></span></div>
  <div class="row tiny" style="left:20px;top:104px;font-size:5.8px"><span style="color:var(--blue)">●</span>&nbsp; Who owns it? &nbsp;<span style="color:var(--blue)">●</span> How long have they owned it? &nbsp;<span style="color:var(--blue)">●</span> Why are they selling it?</div>
  <div class="row" style="left:14px;top:117px;font-size:7.6px"><svg class="tick"><use href="#tick-navy"/></svg><span>What to look for:</span></div>

  <div class="abs" style="left:0;top:146px;width:100%;height:94px;background:var(--navy)"></div>
  <div class="abs tiny white-t" style="left:15px;top:153px;width:150px">
    <p><span class="orange-t">A&nbsp; Poor management</span> - typically by individual owners, families, or out of state management.</p>
    <p style="margin-top:4px"><span class="orange-t">B&nbsp; Under market rents</span> - rates significantly below comparable prices in the area.</p>
    <p style="margin-top:4px"><span class="orange-t">C&nbsp; Deferred maintenance</span> - this can be a sign of a motivated or "burned-out" seller. Light exterior and interior upgrades, e.g., paint, landscaping, carpet replacement, fixture and appliance upgrades, will have a significant impact.</p>
  </div>
  <div class="abs tiny white-t" style="left:182px;top:153px;width:146px">
    <p><span class="orange-t">D&nbsp; High vacancy</span> - Often due to poor marketing.</p>
    <p style="margin-top:5px"><span class="orange-t">E&nbsp; Motivated Sellers</span> - allows for negotiation a lower price. Common motivators include divorce, bankruptcy, retirement, inherited properties, new investment opportunity, burnout, etc.</p>
    <p style="margin-top:5px"><span class="orange-t">F&nbsp; Owner paid utilities</span> - allows for significant upside in income through implementing Ratio Utility Business System (RUBS).</p>
  </div>

  <div class="row" style="left:12px;top:262px;width:325px;font-size:6.2px"><svg class="tick"><use href="#tick-orange"/></svg><span>By tackling these issues, we will successfully reposition the property, which will significantly increase the income. As a result, the value of the property will also increase</span></div>
  <div class="row" style="left:12px;top:294px;width:320px;font-size:7.2px"><svg class="tick"><use href="#tick-orange"/></svg><span><b>Property Class</b> - <span style="font-size:6.2px">B and C class properties in A and B neighborhoods - Prefer 1980's or newer</span></span></div>
  <p class="abs tiny" style="left:25px;top:322px;width:300px">These properties tend to house blue collar workers; don't compete with new(er) construction; and don't share the same challenges as C and D properties in C and D neighborhoods, which can encounter issues with crime, major disrepair, and increased vulnerability to economic downturns.</p>

  <div class="abs" style="left:0;top:357px;width:100%;height:109px;background:var(--band)"></div>
  <div class="row" style="left:12px;top:362px;width:322px;font-size:6.8px"><svg class="tick"><use href="#tick-orange"/></svg><span><b>Market Analysis</b>-Target emerging markets with population and job growth; low to median cost of housing which allows rent growth (e.g., Columbus, Oklahoma, Atlanta, Dallas, Phoenix); median income of ~$35k/ yr; and landlord and business friendly rules and regulations (e.g., Ohio, Texas, Florida, Oklahoma, Colorado).</span></div>
  <p class="abs tiny" style="left:23px;top:410px;width:305px">60+ units to support effective, third-party professional management. Additionally, targeting 60+ units will increase the likelihood of stability by creating a buffer against tenant turnover and other unplanned expenses.</p>
  <p class="abs tiny" style="left:23px;top:435px;width:305px"><b style="color:#333">CASH FLOW</b> - The property must generate cash flow from day one, before value add strategies are deployed.</p>
  <p class="abs tiny" style="left:23px;top:449px;width:305px">Buy on actual numbers instead of on pro forma analysis, which project or estimate financial return</p>
  <div class="footer-bar" style="left:24px;width:294px"></div>
</section>

<!-- Steps: Finance & manage right -->
<section class="page" style="left:816px;top:98px;width:343px;height:480px">
  <div class="frame" style="left:8px;top:8px;width:327px;height:464px"></div>
  <div class="step-title orange" style="left:23px;top:30px"><span style="color:var(--blue)">2</span>&nbsp; FINANCE RIGHT</div>
  <div class="abs" style="left:23px;top:52px;width:306px;font-size:7.2px;line-height:1.7">
    <div style="display:flex"><svg class="tick"><use href="#tick-navy"/></svg><span>Longterm debt - with long terms and amortization periods.</span></div>
    <div style="display:flex"><svg class="tick"><use href="#tick-navy"/></svg><span>Non-recourse if possible. e.g., Hearthstone Lending, Keystone Mortgage, CMBS. There is an extremely low foreclosure rate for Hearthstone and Keystone underwritten properties (1%-2%).</span></div>
    <div style="display:flex"><svg class="tick"><use href="#tick-navy"/></svg><span>No prepayment penalty.</span></div>
    <div style="display:flex"><svg class="tick"><use href="#tick-navy"/></svg><span>No due on sale clause.</span></div>
  </div>
  <div class="photo photo-houses" style="top:147px;height:119px" role="img" aria-label="Blue-toned photo of a row of two-storey townhouses along a street"></div>
  <div class="step-title orange" style="left:21px;top:292px"><span style="color:var(--blue)">3</span>&nbsp; MANAGE RIGHT</div>
  <div class="row" style="left:23px;top:314px;width:300px;font-size:7.2px"><svg class="tick"><use href="#tick-navy"/></svg><span>Third-Party Management with experience in this specific class of multifamily real estate</span></div>
  <div class="abs" style="left:26px;top:339px;width:310px;font-size:5.8px;line-height:1.35">
    <p style="display:flex"><span style="color:var(--blue);width:10px">●</span><span>Sizable but not too large that our property gets lost.</span></p>
    <p style="display:flex;margin-top:5px"><span style="color:var(--blue);width:10px;flex:none">●</span><span>Only in property management, not acquisition or development so that there is no conflict of interest.</span></p>
    <p style="display:flex;margin-top:5px;font-size:7.2px"><span style="color:var(--blue);width:10px">●</span><span>Use of Sole Purpose Entity Structures, e.g., LLC's for asset protection.</span></p>
    <p style="display:flex;margin-top:3px;font-size:7.2px"><span style="color:var(--blue);width:10px">●</span><span>Optimization through use of systems.</span></p>
    <p style="display:flex;margin-top:5px"><span style="color:var(--blue);width:10px;flex:none">●</span><span><span style="font-size:7.2px">Tenant satisfaction</span> - Ensure great customer service to the tenant, e.g., 24 hour response to maintenance requests, cleanliness, and security. Happy tenants who feel heard and cared for, don't leave, which limits tenant turnover, and lowers expenses.</span></p>
    <p style="display:flex;margin-top:6px"><span style="color:var(--blue);width:10px;flex:none">●</span><span><span style="font-size:7.2px">Increase the "curb appeal"</span> - Freshened exterior with modern paint schemes, landscaping, and new signage. Rebranding with a name change, webpage, etc.</span></p>
  </div>
  <div class="footer-bar" style="left:28px;width:287px"></div>
</section>

<!-- Income strategies & ways to profit -->
<section class="page" style="left:239px;top:634px;width:355px;height:497px">
  <div class="frame" style="left:8px;top:8px;width:339px;height:481px"></div>
  <div class="section-head" style="left:18px;top:25px;width:315px;height:26px;font-size:13.5px">5 STRATEGIES FOR INCREASING INCOME</div>
  <div class="abs blue-t" style="left:25px;top:69px;font-size:7.6px">1&nbsp;&nbsp; FILL VACANT UNITS AT MARKET RATE</div>
  <div class="row" style="left:24px;top:83px;width:310px;font-size:6.6px"><svg class="tick" style="width:7px;height:7px"><use href="#tick-orange"/></svg><span>After light renovation (&lt; $1,000 per unit) - modern, two-tone paint schemes (white trim, taupe/light grey walls); vinyl wood plank flooring to replace carpet; cleaning of existing carpet.</span></div>
  <div class="abs blue-t" style="left:25px;top:114px;font-size:7.6px">2&nbsp; EMPLOY RUBS, WHERE APPLICABLE</div>
  <div class="row" style="left:24px;top:128px;width:140px;font-size:6.6px"><svg class="tick" style="width:7px;height:7px"><use href="#tick-orange"/></svg><span>Pre-calculated formula for billing back a tenant's utilities.</span></div>
  <div class="row" style="left:166px;top:128px;width:160px;font-size:6.6px"><svg class="tick" style="width:7px;height:7px"><use href="#tick-orange"/></svg><span>&nbsp;Water, sewer, trash, gas/electric.</span></div>
  <div class="abs blue-t" style="left:25px;top:156px;font-size:7.6px;line-height:1.3">3&nbsp; GRADUALLY RAISE EXISTING TENANTS TO MARKET RATE<br>&nbsp;&nbsp;&nbsp;&nbsp;AFTER ADDING VALUE</div>
  <div class="row" style="left:24px;top:181px;width:310px;font-size:6.6px"><svg class="tick" style="width:7px;height:7px"><use href="#tick-orange"/></svg><span>Improve the exterior "curb appeal" - power washing, landscaping, painting. Inexpensive and effective.</span></div>
  <div class="abs blue-t" style="left:25px;top:214px;font-size:7px">4&nbsp;&nbsp; Fees - Pet fees; deposits; late fees (without exception); move-in fees</div>
  <div class="abs blue-t" style="left:25px;top:232px;font-size:6.8px">5&nbsp;&nbsp; Laundry machines&nbsp;&nbsp; 6&nbsp;&nbsp; Lower expenses through renegotiation of contracts</div>

  <div class="section-head" style="left:18px;top:261px;width:155px;height:26px;font-size:13.5px">5 WAYS TO PROFIT</div>
  <div class="abs" style="left:0;top:297px;width:100%;height:172px;background:var(--band)"></div>
  <div class="abs" style="left:18px;top:303px;width:322px;font-size:7.6px;line-height:1.5;text-align:justify">
    <div style="display:flex"><svg class="tick" style="margin-right:8px"><use href="#tick-orange"/></svg><span><b>Monthly Cash Flow</b> - From day one. Conservative estimation of 9% or higher cash on cash return.</span></div>
    <div style="display:flex"><svg class="tick" style="margin-right:8px"><use href="#tick-orange"/></svg><span><b>Equity through principle pay down</b> - As the tenants pay down the mortgage, your equity continues to increase and creates true wealth.</span></div>
    <div style="display:flex"><svg class="tick" style="margin-right:8px"><use href="#tick-orange"/></svg><span>Reduced or even elimination of taxes through depreciation by doing cost segregation</span></div>
    <div style="display:flex"><svg class="tick" style="margin-right:8px"><use href="#tick-orange"/></svg><span><b>Cash out refinancing</b> -into non-recourse debt (if not already); return of original capital plus additional monies that can be used towards reinvestment into the asset and future assets.</span></div>
    <div style="display:flex"><svg class="tick" style="margin-right:8px"><use href="#tick-orange"/></svg><span><b>Forced Appreciation</b> - by repositioning the asset through the methods previously discussed. Potential to double the original investment at the time of sale, which could occur in 5-7 years or sooner depending on the market.</span></div>
  </div>
  <div class="footer-bar" style="left:29px;width:297px"></div>
</section>

<!-- Back cover -->
<section class="page" style="left:626px;top:631px;width:357px;height:500px">
  <div class="frame" style="left:10px;top:10px;width:337px;height:480px"></div>
  <div class="photo photo-houses" style="top:0;height:214px" role="img" aria-label="Blue-toned photo of a row of townhouses with pitched roofs under a cloudy sky"></div>
  <div class="abs" style="left:32px;top:145px;width:148px;height:148px;border-radius:50%;background:radial-gradient(circle at 50% 45%,#c9c2ba 0%,#8b8078 60%,#4c4541 100%);border:3px solid #fff" role="img" aria-label="Circular black-and-white headshot of the investor"></div>
  <p class="abs brand-name" style="left:30px;top:340px;width:175px;font-family:'Montserrat',sans-serif;font-weight:600;font-size:21px;line-height:1.2;color:var(--navy);letter-spacing:.02em">REDMONT<br>RESIDENTIAL</p>
  <p class="abs" style="left:211px;top:334px;width:124px;font-family:'Lato',sans-serif;font-size:5.4px;line-height:1.55;color:#333;text-align:justify">Marisa Holloway is a real estate investor and physician with a passion for identifying and fixing problems through innovative and creative solutions. Her transition into commercial real estate is merely an extension of that passion. It is her professional experience in a demanding and competitive field, along with her tenacity and discipline for doing things effectively and efficiently, which instills confidence in her success as a CRE investor.</p>
  <div class="footer-bar" style="left:29px;width:300px"></div>
</section>

</body>
</html>
```